Ridgeline Wild Craft DL flyer

I'm looking for a new flyer for my startup business. In Darwin Australia.
Aimed at family's and short stay tourists the "Ridgeline Wild Craft" 4 hr tour will give people a basic understanding of some essential bush survival skills in the Australian Outback.
things covered in this 4 hr tour are
1. Finding water.
2. finding food.
3. Finding/making shelter and fire.
4. Finding your way home.

The tour will pick clients up in an air conditioned purpose build 4WD and take them to a nearby bushland area where they will have the opportunity to catch and harvest some native bushtucker.
They will then be able to find/harvest some water for survival situations.
While we cook our bush tucker they will also learn to find their way home through ancient navigation techniques as well.

Clients will then be dropped back to their accomodation with some fun and vital knowledge of surviving in the Australian outback.
At the end of the tour the group will be able to take home a basic survival kit which they will be able to use through the skills they just gained on the tour.

I'd like a two sided DL size flyer emphasising the following points.
4hr/half day tour
Fun for the family
Free survival kit included.
Eat what you catch
Learn essential survival skills
Provided buy an experienced and passionate bushman.
$150/head including transfers.

I'll provide some pictures for the flyer and any extra content you require.

Target Market(s)

Family's
Short stay tourists

Industry/Entity Type

Tourism

Colors

Designer to choose colors to be used in the design.

Requirements
Must have
• As per brief
Nice to have
• Any extra content and flair designers would like to add
Should not have
• Any images which aren't Australian

```html
<!DOCTYPE html>
<html lang="en">
<head>
<meta charset="utf-8">
<title>Ridgeline Wild Craft – DL Flyer</title>
<link href="https://fonts.googleapis.com/css2?family=Caprasimo&display=swap" rel="stylesheet">
<style>
  :root{
    --stage:#58585a;
    --orange:#f05a2b;
    --blue:#0a77bf;
    --ink-grey:#58585a;
    --paper:#ffffff;
    --paper-shade:#e9e9ea;
  }
  *{margin:0;padding:0;box-sizing:border-box}
  html,body{width:1200px;height:801px;overflow:hidden}
  body{background:var(--stage);position:relative;font-family:"Caprasimo",Georgia,serif}

  .panel{position:absolute;top:60px;width:320px;height:679px;overflow:hidden;
    background:linear-gradient(90deg,var(--paper-shade) 0%,var(--paper) 45%,var(--paper) 100%);
    box-shadow:5px 5px 6px rgba(0,0,0,.45)}
  .panel--front{left:256px}
  .panel--back{left:624px;width:319px}

  .photo{position:absolute}
  .photo--hero-front{left:0;top:0;width:320px;height:242px;
    background:linear-gradient(160deg,#6b5a44 0%,#8d735a 40%,#d7b59a 60%,#4f4536 100%)}
  .photo--hero-back{left:0;top:0;width:319px;height:348px;
    background:linear-gradient(180deg,#f4f5f2 0%,#c9c8b8 35%,#7d8a6a 65%,#9fa08f 100%)}

  .band-blue{position:absolute;left:0;width:100%;background:var(--blue)}

  .thumb{position:absolute;width:148px;height:92px;border:3px solid var(--orange);border-radius:10px;overflow:hidden}
  .thumb__img{width:100%;height:100%}

  .front-kicker{position:absolute;left:0;width:100%;top:334px;text-align:center;
    color:var(--ink-grey);font-size:31px;line-height:1}
  .front-rule{position:absolute;left:42px;width:240px;top:379px;height:2px;
    background:linear-gradient(90deg,transparent,var(--ink-grey) 15%,var(--ink-grey) 85%,transparent)}
  .front-title{position:absolute;left:0;width:100%;top:384px;text-align:center;
    color:var(--blue);font-size:74px;line-height:1;letter-spacing:1px}

  .band-orange{position:absolute;left:0;width:100%;bottom:0;background:var(--orange)}
  .front-tagline{position:absolute;left:0;width:100%;top:588px;text-align:center;
    color:#fff;font-size:30px;line-height:40px}

  .offer-list{position:absolute;left:34px;top:449px;list-style:none;color:var(--orange);
    font-size:13.6px;line-height:21.5px}
  .offer-list li{position:relative;padding-left:13px}
  .offer-list li::before{content:"";position:absolute;left:0;top:7px;width:8px;height:8px;border-radius:50%;background:var(--blue)}

  .contact{position:absolute;left:0;width:100%;top:632px;text-align:center;color:#fff;font-size:11.5px;line-height:17px}
</style>
</head>
<body>

<section class="panel panel--front" aria-label="Flyer front">
  <div class="photo photo--hero-front" role="img" aria-label="Hands holding a blue-clawed freshwater crayfish"></div>
  <div class="band-blue" style="top:242px;height:9px"></div>

  <div class="thumb" style="left:10px;top:216px">
    <div class="thumb__img" role="img" aria-label="Hand holding green native bush fruit" style="background:linear-gradient(135deg,#d9a99a,#9aa25a,#e2b9a8)"></div>
  </div>
  <div class="thumb" style="left:162px;top:216px">
    <div class="thumb__img" role="img" aria-label="Termite mounds in green outback grassland" style="background:linear-gradient(180deg,#d7e3d6 0%,#6f7f4a 40%,#a0563a 60%,#5f8c32 100%)"></div>
  </div>

  <p class="front-kicker">4hr/Half Day</p>
  <div class="front-rule"></div>
  <h1 class="front-title">TOUR</h1>

  <div class="band-blue" style="top:553px;height:3px"></div>
  <div class="band-orange" style="height:117px"></div>

  <div class="thumb" style="left:10px;top:484px">
    <div class="thumb__img" role="img" aria-label="Stick shadow navigation marked east and west on dirt" style="background:linear-gradient(135deg,#8a6a45,#b18f62,#7d5f3c)"></div>
  </div>
  <div class="thumb" style="left:162px;top:484px">
    <div class="thumb__img" role="img" aria-label="Plastic sheet water trap over green plants" style="background:linear-gradient(160deg,#1f3a1c 0%,#dfe6e6 50%,#4f9a2c 100%)"></div>
  </div>

  <p class="front-tagline">FUN FOR<br>THE FAMILY</p>
</section>

<section class="panel panel--back" aria-label="Flyer back">
  <div class="photo photo--hero-back" role="img" aria-label="Experienced bushman in wide-brim hat and sunglasses in the bush"></div>
  <div class="band-blue" style="top:348px;height:6px"></div>

  <div class="thumb" style="left:12px;top:326px">
    <div class="thumb__img" role="img" aria-label="Orange bush fruit on a branch by the coast" style="background:linear-gradient(160deg,#6d86a8 0%,#8a6a4a 50%,#d08a2a 70%,#7a6a55 100%)"></div>
  </div>
  <div class="thumb" style="left:166px;top:326px">
    <div class="thumb__img" role="img" aria-label="Pandanus palm leaves" style="background:linear-gradient(140deg,#e9eee2 0%,#5f8a3a 45%,#8a6a3a 70%,#3f6a2a 100%)"></div>
  </div>

  <ul class="offer-list">
    <li>Free survival kit included.</li>
    <li>Eat what you catch</li>
    <li>Learn essential survival skills</li>
    <li>Provided buy an experienced<br>and passionate bushman.</li>
    <li>$150/head including transfers.</li>
  </ul>

  <div class="band-blue" style="top:602px;height:4px"></div>
  <div class="band-orange" style="height:70px"></div>
  <p class="contact">Contat us:<br>+00 000 0000 | Email:hello@ridgelinewildcraft.com</p>
</section>

</body>
</html>
```